Child sleep consultant needs a flyer to attract new clients

We need a flyer that will attract the attention of parents with children between newborn and 3 years old who may be experiencing sleep issues. The flyer will be placed at places such as community centres, doctors room, play centres, etc.

Our business is called Hushwood Nestlings and provides a sleep consultancy service. Our service essentially provides a routine for parents to follow and general advice. Our service is not medical advice.

We need the flyer to have an overall tone that is soft and peaceful however can catch the attention of parents who may be struggling on minimal sleep. We would like photos with minimal text. The colour we use is green.

We will provide the text to appear in the flyer once we have a better idea of the layout that we prefer for the flyer. The text however wont be extensive, just some catchy points.

We want to direct people to our website which is hushwoodnestlings.com.au. We also have a facebook page, which is Hushwood Nestlings.

We have a logo that we would like to appear on the flyer. We will attach the file once the uploader on pixel bazaar is fixed.

Our consultant is a certified Dream Anchor consultant, which has a separate logo that should appear somewhere on the logo. I will attach this once the uploader is fixed.

When we print the flyer - we want to print A5 SIZE ... please make sure the formatting is OK for this size.

Target Market(s)

Mums and Dads with children between newborn and 3 years old.

Industry/Entity Type

Consultant

Colors
cadf82

Requirements
Must have
• - Our logo.
• - Dream Anchor consultant logo - both attached to this brief.
• - Contact details - including phone number, email address and website
• - MUST be suitable for A5 printable size, double sided please.
• Must have the following text:
• If your baby or toddler isn't sleeping through the night, neither are you - and this means you are probably feeling physically and mentally exhausted, stressed, depressed and irritable, afraid you might be damaging your child and disconnected from your partner.
• The good news is nearly all healthy children 3 months or older are physically capable of sleeping 12 solid hours without waking. They just need to be taught the healthy sleep habits that enable them to do so.
• I can help with the sleep issues your child is experiencing. As a certified Dream Anchor (insert trademark TM here) I can help if:
• - your child will only fall asleep when nursing or bottle feeding
• - your child needs a dummy in order fall asleep
• - you're waking up with your child one or more times per night
• - your child needs to be rocked, patted, or taken for a car ride to go to sleep
• - your own lack of sleep is starting to take a toll on your family
• I've been personally trained by Marla Penwick, best selling author of the Dream Anchor (insert trade mark symbol here) Program to teach her sleep training methods to families like yours. Marla's methods have already helped over 30,000 parents and children and I'd be delighted to help your family next!
• Call or email for a free 15 minute consultation
• I would love to connect with you to talk about your child's specific situation and discuss different solutions.

```html
<!DOCTYPE html>
<html lang="en">
<head>
<meta charset="utf-8">
<title>Hushwood Nestlings – Sleep Consultant Flyer</title>
<link rel="stylesheet" href="https://fonts.googleapis.com/css2?family=PT+Sans:wght@400;700&family=PT+Sans+Narrow:wght@700&display=swap">
<style>
  :root {
    --green-top: #a5d463;
    --green-mid: #c3df8a;
    --green-low: #d3e6a6;
    --white: #ffffff;
    --olive-text: #4e5a1c;
    --contact-green: #8bb63a;
    --logo-green: #8fb25a;
    --star-purple: #9b59b6;
    --badge-pink: #f283bd;
    --dark-text: #1c1c1c;
    --photo-skin: #f1c7b0;
    --photo-hat: #b98bc4;
    --photo-rug: #efe2d8;
  }
  * { box-sizing: border-box; margin: 0; padding: 0; }
  html, body {
    width: 1200px; height: 1000px; overflow: hidden;
    background: var(--white);
    font-family: "PT Sans", sans-serif;
  }
  .canvas { position: relative; width: 1200px; height: 1000px; }
  .flyer {
    position: absolute; left: 251px; top: 0; width: 698px; height: 1000px;
    background: linear-gradient(180deg, var(--green-top) 0%, var(--green-mid) 45%, var(--green-low) 70%);
    overflow: hidden;
  }
  .photo-area {
    position: absolute; left: 0; top: 520px; width: 698px; height: 480px;
    background:
      radial-gradient(ellipse 150px 130px at 480px 150px, var(--photo-hat) 0%, rgba(185,139,196,0.6) 60%, rgba(185,139,196,0) 100%),
      radial-gradient(ellipse 260px 170px at 360px 300px, var(--photo-skin) 0%, rgba(241,199,176,0.7) 60%, rgba(241,199,176,0) 100%),
      linear-gradient(180deg, rgba(211,230,166,0) 0%, rgba(239,226,216,0.7) 60%, var(--photo-rug) 100%);
  }
  .brand-mark {
    position: absolute; left: 271px; top: 60px; width: 156px; height: 156px;
    border-radius: 50%; background: var(--white);
    display: flex; align-items: center; justify-content: center; text-align: center;
  }
  .brand-name {
    font-family: "PT Sans", sans-serif; font-weight: 400;
    font-size: 21px; line-height: 1.05; color: var(--logo-green); width: 110px;
  }
  .headline {
    position: absolute; left: 0; top: 236px; width: 698px; text-align: center;
    color: var(--white); font-weight: 700; font-size: 18px; line-height: 22px;
    text-transform: uppercase;
  }
  .cert-badge { position: absolute; left: 303px; top: 290px; width: 92px; height: 46px; }
  .help-title {
    position: absolute; left: 0; top: 344px; width: 698px; text-align: center;
    color: var(--white); font-weight: 700; font-size: 16px;
  }
  .help-list {
    position: absolute; left: 0; top: 382px; width: 698px; list-style: none;
    text-align: center; color: var(--white); font-size: 14.5px; line-height: 18.6px;
  }
  .help-list .star { color: var(--star-purple); font-size: 10px; vertical-align: 2px; margin: 0 5px; }
  .trainer-note {
    position: absolute; left: 62px; top: 493px; width: 450px;
    color: var(--olive-text); font-weight: 700; font-size: 13.6px; line-height: 16.2px;
  }
  .offer-badge {
    position: absolute; left: 63px; top: 592px; width: 152px; height: 152px;
  }
  .offer-text {
    position: absolute; left: 63px; top: 628px; width: 152px; text-align: center;
    font-family: "PT Sans Narrow", sans-serif; font-weight: 700; color: var(--white);
    font-size: 14px; line-height: 14px; text-transform: uppercase;
  }
  .offer-text .big { display: block; font-size: 24px; line-height: 24px; font-style: italic; }
  .connect-note {
    position: absolute; left: 44px; top: 750px; width: 190px; text-align: center;
    color: var(--dark-text); font-weight: 700; font-size: 12px; line-height: 14.5px;
  }
  .contact {
    position: absolute; right: 59px; top: 887px; text-align: right;
    color: var(--contact-green); font-weight: 700; font-size: 12px; line-height: 14.5px;
  }
</style>
</head>
<body>
<div class="canvas">
  <section class="flyer">
    <div class="photo-area" role="img" aria-label="Photo of a sleeping newborn wearing a purple felt flower hat, lying on a soft pale rug"></div>

    <div class="brand-mark"><span class="brand-name">Hushwood Nestlings</span></div>

    <h1 class="headline">I can help with the sleep issues your child is experiencing.<br>As a certified Dream Anchor consultant</h1>

    <svg class="cert-badge" viewBox="0 0 92 46" role="img" aria-label="Certified Dream Anchor consultant badge">
      <rect x="4" y="6" width="84" height="34" rx="6" fill="#e9f2d2"/>
    </svg>

    <h2 class="help-title">I can help if:</h2>

    <ul class="help-list">
      <li><span class="star">★</span>Your child will only fall asleep when nursing or bottle feeding<span class="star">★</span></li>
      <li><span class="star">★</span>Your child needs a dummy in order to fall asleep<span class="star">★</span></li>
      <li><span class="star">★</span>You’re waking up with your child one or more times per night<span class="star">★</span></li>
      <li><span class="star">★</span>Your child needs to be rocked, patted, or taken for a car ride to go to sleep<span class="star">★</span></li>
      <li><span class="star">★</span>Your own lack of sleep is starting to take a toll on your family<span class="star">★</span></li>
    </ul>

    <p class="trainer-note">I've been personally trained by Marla Penwick, best selling author of the Dream Anchor™ Program to teach her sleep training methods to families like yours. Marla's methods have already helped over 30,000 parents and children and I'd be delighted to help your family next!</p>

    <svg class="offer-badge" viewBox="0 0 152 152" aria-hidden="true">
      <g fill="var(--badge-pink)">
        <circle cx="76" cy="76" r="62"/>
        <circle cx="76" cy="20" r="20"/><circle cx="76" cy="132" r="20"/>
        <circle cx="20" cy="76" r="20"/><circle cx="132" cy="76" r="20"/>
        <circle cx="36" cy="36" r="20"/><circle cx="116" cy="36" r="20"/>
        <circle cx="36" cy="116" r="20"/><circle cx="116" cy="116" r="20"/>
      </g>
    </svg>
    <p class="offer-text">Call or email<br>for a free<span class="big">15</span>minute<br>consultation</p>

    <p class="connect-note">I would love to connect with you to talk about your child's specific situation and discuss different solutions.</p>

    <address class="contact" style="font-style:normal">
      Tel.: 0400 - 517 - 302<br>
      E-mail: hello@hushwoodnestlings.com.au<br>
      www.hushwoodnestlings.com.au<br>
      facebook.com/hushwoodnestlings
    </address>
  </section>
</div>
</body>
</html>
```